Modern and Simple Supplement Label Design

We are looking for a Professional Graphic Designer who can design eye-catching and unique supplement label. We are supplement company who are sourcing different supplement products. I would like the design to be simple and with few colorsThe final design should communicate strength and growthI attached some samples for inspiration

Target Market(s)

Supplement Market - Collagen Supplements

Industry/Entity Type

Supplement

Font styles to use
Serif
Sans Serif

Colors

Designer to choose colors to be used in the design.

Requirements
Must have
• Front (Please search on Ombrix Collagen to get inspiration how to put together the front text)
• Logo: Velko Naturals
• Product Name: Duravita Blend Capsules
• Hydrolyzed type I II III V & X Collagen
• Dietary Supplements - 90 capsules
• Support Joints & bones
• Rejuvenate Skin
• Promotes Healthy Hair & Nails
• One right side supplement fact and left side precaution and instruction content. ( Please find the content of the right and left side of the bottle attached)
Nice to have
• Nice to have something that shows elements bring together to create something strong or beautiful. Our brand name is Velko Naturals. Velko is an assembly of beams or other elements that creates a rigid structure. This is to show our supplements help to provide the elements to have strong and healthy life

```html
<!DOCTYPE html>
<html lang="en">
<head>
<meta charset="utf-8">
<title>Velko Naturals – Duravita Blend Capsules Label</title>
<link href="https://fonts.googleapis.com/css2?family=Montserrat:wght@400;500;600;700;800&family=Oswald:wght@400;500;600&family=Kaushan+Script&display=swap" rel="stylesheet">
<style>
  :root{
    --page:#e9e9ea;
    --label:#f4f4f5;
    --panel:#ececed;
    --ink:#161616;
    --text:#2b2b2b;
    --muted:#555;
    --rule:#9a9a9a;
    --orange:#e8873a;
    --leaf:#6cb33f;
    --gold:#d9a521;
    --gold-dark:#9c7312;
    --silver-light:#ffffff;
    --silver-mid:#c9cacc;
    --silver-dark:#8d8f93;
    --capsule-1:#ffd24a;
    --capsule-2:#e09a12;
  }
  *{box-sizing:border-box;margin:0;padding:0}
  html,body{width:1082px;height:1200px;overflow:hidden;background:var(--page)}
  .canvas{position:relative;width:1082px;height:1200px}
  .label{
    position:absolute;left:20px;top:387px;width:1434px;height:585px;
    transform:scale(0.7266);transform-origin:top left;
    background:var(--label);overflow:hidden;font-family:"Montserrat",sans-serif;color:var(--text);
  }
  .shape-layer{position:absolute;inset:0}
  .abs{position:absolute}

  /* left side */
  .info-box{position:absolute;left:52px;width:331px;border:1px solid var(--rule);padding:10px 14px;font-size:11.5px;line-height:1.3;background:rgba(255,255,255,.35)}
  .info-title{position:absolute;top:-12px;left:28px;background:var(--label);padding:0 4px;font-weight:600;font-size:12.5px;letter-spacing:.3px;color:var(--ink)}
  .info-title::after{content:"";display:inline-block;width:8px;height:8px;border-radius:50%;background:var(--leaf);margin-left:3px;vertical-align:4px}
  .warning-box{font-family:"Oswald",sans-serif;font-weight:500;text-align:center;font-size:14px;line-height:1.45;text-transform:uppercase;color:var(--ink);letter-spacing:-.3px}
  .icons{position:absolute;left:165px;top:375px;display:flex;gap:18px}
  .disclaimer{font-size:9.5px;text-align:center;padding:5px 10px;line-height:1.3}
  .lot{left:80px;top:550px;font-size:9.5px;font-weight:600;color:var(--ink)}

  /* brand */
  .brand{display:flex;align-items:center;gap:6px;font-family:"Montserrat",sans-serif;font-weight:800;color:var(--ink);white-space:nowrap}
  .brand-dot{width:12px;height:12px;border-radius:50%;background:var(--leaf)}

  /* front */
  .front{position:absolute;left:500px;width:460px;text-align:center}
  .name-top{top:98px;font-family:"Montserrat",sans-serif;font-weight:500;font-size:46px;color:var(--orange);letter-spacing:1px}
  .name-main{top:152px;font-family:"Montserrat",sans-serif;font-weight:800;font-size:62px;color:var(--ink);letter-spacing:-1px}
  .name-script{top:228px;font-family:"Kaushan Script",cursive;font-size:50px;color:var(--orange)}
  .divider{top:302px;left:640px;width:180px;height:1px;background:var(--rule);position:absolute}
  .benefit{font-family:"Oswald",sans-serif;font-weight:500;font-size:21px;color:var(--ink);line-height:1.35}
  .dot{width:9px;height:9px;border-radius:50%;background:var(--orange);margin:0 auto}
  .dietary{top:528px;font-family:"Montserrat",sans-serif;font-weight:600;font-size:18px;letter-spacing:1.5px;color:var(--ink)}
  .types{top:553px;font-size:14.5px;color:var(--ink)}
  .count-badge{left:541px;top:446px;width:84px;height:84px;border-radius:50%;
    background:radial-gradient(circle at 40% 35%,#fff3b8,var(--gold) 55%,var(--gold-dark));
    display:flex;flex-direction:column;align-items:center;justify-content:center;border:3px solid #f4f4f4;box-shadow:0 1px 3px rgba(0,0,0,.35)}
  .count-num{font-family:"Oswald",sans-serif;font-weight:600;font-size:40px;line-height:1;color:var(--ink)}
  .count-word{font-family:"Kaushan Script",cursive;font-size:12px;color:var(--ink);transform:rotate(-14deg);margin-top:-2px}
  .seal{width:44px;height:44px;border-radius:50%;background:#2c2c2c;border:3px solid #e2e2e2;box-shadow:0 0 0 1px #444}

  /* right side */
  .facts{left:1044px;top:142px;width:339px;border:2px solid var(--ink);border-radius:4px;padding:6px 8px;background:rgba(255,255,255,.4);font-family:"Oswald",sans-serif;color:var(--ink)}
  .facts h2{font-family:"Oswald",sans-serif;font-weight:600;font-size:40px;line-height:1.05;letter-spacing:-.5px}
  .facts .serving{font-size:16.5px;line-height:1.45;padding-left:6px}
  .bar-thick{height:9px;background:var(--ink);margin:6px 0 4px}
  .bar-thin{height:1px;background:var(--ink)}
  .row{display:flex;font-size:14px}
  .facts table{width:100%;border-collapse:collapse}
  .amount-head{font-size:13.5px;text-align:right;padding:3px 0}
  .nutrient{font-size:15.5px;line-height:1.3;padding:6px 6px}
  .sources{font-size:11.5px;line-height:1.75;padding:4px 6px 6px;border-top:1px solid var(--ink)}
  .footnote{font-size:13.5px;padding:6px 6px 2px}
  .extras{left:1053px;top:462px;list-style:none;font-family:"Oswald",sans-serif;font-size:14.5px;color:var(--ink);line-height:1.45}
  .extras li::before{content:"";display:inline-block;width:6px;height:6px;border-radius:50%;background:var(--ink);margin-right:8px;vertical-align:3px}
</style>
</head>
<body>
<div class="canvas">
  <div class="label">
    <svg class="shape-layer" width="1434" height="585" viewBox="0 0 1434 585" aria-hidden="true">
      <defs>
        <linearGradient id="silverLeft" x1="0" x2="1" y1="0" y2="0">
          <stop offset="0" stop-color="var(--silver-dark)"/>
          <stop offset=".45" stop-color="var(--silver-light)"/>
          <stop offset="1" stop-color="var(--silver-mid)"/>
        </linearGradient>
        <linearGradient id="silverRight" x1="1" x2="0" y1="0" y2="0">
          <stop offset="0" stop-color="var(--silver-dark)"/>
          <stop offset=".45" stop-color="var(--silver-light)"/>
          <stop offset="1" stop-color="var(--silver-mid)"/>
        </linearGradient>
      </defs>
      <path d="M385 0 C470 120 500 200 505 330 C510 450 520 530 520 585 L590 585 C585 500 560 420 560 320 C560 200 510 90 440 0 Z" fill="url(#silverLeft)"/>
      <path d="M1080 0 C1000 100 930 200 910 320 C895 430 890 520 890 585 L925 585 C925 500 935 420 955 330 C985 200 1040 100 1100 0 Z" fill="url(#silverRight)"/>
      <path d="M440 0 C510 90 560 200 560 320 C560 420 585 500 590 585 L890 585 C890 520 895 430 910 320 C930 200 1000 100 1080 0 Z" fill="var(--panel)"/>
    </svg>

    <!-- left side: directions and cautions -->
    <div class="info-box" style="top:52px;height:90px">
      <span class="info-title">SUGGESTED USE</span>
      Take three (3) capsules one or more times a day or as directed by your heath care professional. For best results take on an empty stomach with an a 8oz. glass of water.
    </div>
    <div class="info-box" style="top:163px;height:90px">
      <span class="info-title">CAUTION</span>
      Do not exceed recommended dose. Pregnant or nursing mothers, children under the age of 18, and individuals with a known medical condition should consult a physician before using this or any dietary supplement.
    </div>
    <div class="info-box warning-box" style="top:273px;height:90px;padding-top:12px">
      Keep out of reach of children.<br>Do not use if safety seal is damaged or missing.<br>Store in a cool, dry place.
    </div>
    <div class="icons">
      <svg width="26" height="24" viewBox="0 0 26 24" aria-label="warning"><path d="M13 2 L24 22 H2 Z" fill="none" stroke="var(--ink)" stroke-width="2"/><rect x="12" y="9" width="2" height="7" fill="var(--ink)"/><rect x="12" y="18" width="2" height="2" fill="var(--ink)"/></svg>
      <svg width="24" height="24" viewBox="0 0 24 24" aria-label="recycle"><circle cx="12" cy="12" r="8" fill="none" stroke="var(--ink)" stroke-width="3" stroke-dasharray="11 5"/></svg>
      <svg width="20" height="26" viewBox="0 0 20 26" aria-label="dispose in bin"><circle cx="6" cy="4" r="3" fill="var(--ink)"/><path d="M4 8 L9 8 L8 18 L4 18 Z" fill="var(--ink)"/><path d="M10 12 H19 L17 25 H12 Z" fill="var(--ink)"/></svg>
    </div>
    <div class="info-box disclaimer" style="top:412px;height:44px">
      These statements have not been evaluated by the Food and Drug Administration. This product is not intended to diagnose, treat, cure or prevent any disease.
    </div>
    <div class="abs lot">LOT# and Expiration date printed on bottom of Bottle. KELN</div>

    <!-- front panel -->
    <div class="abs brand" style="left:638px;top:38px;font-size:30px"><span class="brand-dot"></span>Velko Naturals</div>
    <div class="abs front name-top">DURAVITA</div>
    <div class="abs front name-main">BLEND</div>
    <div class="abs front name-script">Capsules</div>
    <div class="divider"></div>
    <div class="abs front" style="top:326px">
      <div class="benefit">SUPPORT JOINTS &amp; BONES</div>
      <div class="dot" style="margin-top:14px;margin-bottom:12px"></div>
      <div class="benefit">REJUVENATE SKIN</div>
      <div class="dot" style="margin-top:14px;margin-bottom:12px"></div>
      <div class="benefit">PROMOTES HEALTHY<br>HAIR &amp; NAILS</div>
    </div>
    <div class="abs front dietary">DIETARY SUPPLEMENTS</div>
    <div class="abs front types">Hydrolyzed type I II III V &amp; X Collagen</div>
    <div class="abs" role="img" aria-label="Golden softgel capsules" style="left:440px;top:300px;width:170px;height:120px;border-radius:50%;background:radial-gradient(ellipse at 50% 50%,var(--capsule-1),var(--capsule-2) 60%,rgba(224,154,18,0) 72%)"></div>
    <div class="abs count-badge"><span class="count-num">90</span><span class="count-word">Capsules</span></div>
    <div class="abs seal" style="left:913px;top:264px"></div>
    <div class="abs seal" style="left:913px;top:328px"></div>
    <div class="abs seal" style="left:913px;top:394px"></div>
    <div class="abs seal" style="left:913px;top:460px"></div>
    <div class="abs seal" style="left:913px;top:526px"></div>

    <!-- right side: supplement facts -->
    <div class="abs" role="img" aria-label="Golden softgel capsules" style="left:1280px;top:0;width:154px;height:85px;background:radial-gradient(ellipse at 60% 40%,var(--capsule-1),var(--capsule-2) 55%,rgba(224,154,18,0) 75%)"></div>
    <div class="abs brand" style="left:1140px;top:70px;font-size:26px"><span class="brand-dot"></span>Velko Naturals</div>
    <div class="abs facts">
      <h2>Supplement Facts</h2>
      <div class="serving">Serving Size: 3 Capsules<br>Servings Per Container: 30</div>
      <div class="bar-thick"></div>
      <div class="amount-head">Amount Per Serving &nbsp;&nbsp;&nbsp;&nbsp;&nbsp; %DV</div>
      <div class="bar-thin"></div>
      <table>
        <tr>
          <td class="nutrient">Premium Collagen<br>Protein Complex</td>
          <td class="nutrient" style="vertical-align:top;text-align:center">1500mg</td>
          <td class="nutrient" style="vertical-align:top;text-align:right">**</td>
        </tr>
      </table>
      <div class="sources">Bovine Collagen Peptides, Hydrolyzed chicken Collagen Peptides. Pure Hydrolyzed Marine Collagen Peptides, Eggshel Membrane Collagen Peptides, Avian Sternum Collagen Peptides.</div>
      <div class="bar-thick" style="margin:0"></div>
      <div class="footnote">** Daily Value not established (DV)</div>
    </div>
    <ul class="abs extras">
      <li>Inactive Ingradients: Gelatin Capsules</li>
      <li>Contains: Egg, Fish</li>
      <li>Contains no added; Milk, Tree Nuts, Wheat, Peanuts, Soy</li>
    </ul>
  </div>
</div>
</body>
</html>
```